ASSET BASED PROGRAM FLIER

Need flier to market hard money loan products offered HARD MONEY FIX & FLIP PROGRAMS

We offer a variety of loan programs Some program highlights include......

1) No Minimum Credit Score
2) 3-5 Day Close
3) Up to 100% of Purchase & Rehab
4) Rates as Low as 7%
5) Loans Offered Nationwide

Contact us today for more information at (800) 647-2915 x42 or email us at mwelton@brightlanefunding.example NMLS #731856 www.brightlanefunding.example

```html
<!DOCTYPE html>
<html lang="en">
<head>
<meta charset="utf-8">
<title>Hard Money Fix &amp; Flip Programs</title>
<link rel="stylesheet" href="https://fonts.googleapis.com/css2?family=Oswald:wght@500&family=Signika:wght@400;500&display=swap">
<style>
  :root{
    --blue:#1566b0;
    --blue-deep:#0d5aa6;
    --blue-light:#1e8fd3;
    --gold:#c4b02e;
    --gold-text:#c7b23a;
    --panel:rgba(190,170,35,.92);
    --ink:#2b2b2b;
    --white:#ffffff;
  }
  *{margin:0;padding:0;box-sizing:border-box}
  html,body{width:993px;height:1200px;overflow:hidden;background:var(--white)}
  .flyer{position:relative;width:993px;height:1200px;overflow:hidden;background:var(--white);font-family:"Signika",sans-serif}
  .hero-photo{position:absolute;left:0;top:0;width:993px;height:580px;
    background:linear-gradient(100deg,#ffffff 0%,#ffffff 36%,#e9e2d6 50%,#b98a6a 64%,#8c3b3b 78%,#6d4a49 100%)}
  .hero-fade{position:absolute;left:0;top:0;width:993px;height:580px;
    background:linear-gradient(180deg,rgba(255,255,255,.95) 0%,rgba(255,255,255,.6) 45%,rgba(255,255,255,0) 70%)}
  .lower-photo{position:absolute;left:0;top:575px;width:993px;height:510px;
    background:linear-gradient(90deg,#f6f6f6 0%,#eceae6 50%,#e3e1dd 100%)}
  .headline{position:absolute;left:49px;top:50px;font-family:"Oswald",sans-serif;font-weight:500;
    font-size:70px;line-height:74px;color:var(--blue);text-transform:uppercase}
  .headline .accent{color:var(--gold)}
  .highlights{position:absolute;left:47px;top:556px;width:904px;height:327px;border-radius:22px;background:var(--panel)}
  .feature{position:absolute;width:200px;text-align:center;color:var(--white);font-size:20px;line-height:25px}
  .feature .badge{display:block;margin:0 auto;width:118px;height:118px}
  .contact{position:absolute;left:492px;top:918px;color:var(--ink)}
  .contact .lead{font-size:21px}
  .contact .phone{font-family:"Oswald",sans-serif;font-weight:500;font-size:57px;line-height:70px;color:var(--gold-text);letter-spacing:-1px}
  .contact .email{font-size:21px}
  .contact .email b{font-weight:500}
  .contact .nmls{font-size:21px;margin-top:10px;margin-left:5px}
  .brand{position:absolute;left:78px;top:975px;display:flex;align-items:center;gap:12px;
    font-size:30px;font-weight:500;color:var(--blue)}
  .brand .dot{width:30px;height:30px;border-radius:50%;background:var(--gold)}
  .footer-band{position:absolute;left:0;top:1075px;width:993px;height:125px}
  .website{position:absolute;left:0;top:1135px;width:993px;text-align:center;color:var(--white);
    font-size:35px;letter-spacing:2px;font-weight:500}
</style>
</head>
<body>
<div class="flyer">
  <div class="hero-photo" role="img" aria-label="Smiling construction worker in a yellow hard hat and plaid shirt carrying lumber on his shoulder at a job site"></div>
  <div class="hero-fade"></div>
  <div class="lower-photo" role="img" aria-label="Faded photo of a worker at a building site"></div>

  <h1 class="headline">Hard Money<br><span class="accent">Fix &amp; Flip</span><br>Programs</h1>

  <div class="highlights">
    <div class="feature" style="left:36px;top:28px">
      <svg class="badge" viewBox="0 0 118 118"><circle cx="59" cy="59" r="48" fill="none" stroke="#fff" stroke-width="4"/>
        <g fill="#fff"><rect x="37" y="46" width="7" height="28"/><rect x="48" y="56" width="7" height="18"/><rect x="59" y="50" width="7" height="24"/><rect x="70" y="42" width="7" height="32"/></g>
        <path d="M42 60 L56 46 L64 52 L76 38" stroke="#fff" stroke-width="3" fill="none"/><path d="M70 36 L79 35 L78 44Z" fill="#fff"/></svg>
      No Minimum<br>Credit Score
    </div>
    <div class="feature" style="left:195px;top:130px">
      <svg class="badge" viewBox="0 0 118 118"><circle cx="59" cy="59" r="48" fill="none" stroke="#fff" stroke-width="4"/>
        <path d="M38 58 L59 40 L80 58 L75 58 L75 76 L43 76 L43 58Z" fill="#fff"/>
        <circle cx="59" cy="63" r="8" fill="none" stroke="var(--gold)" stroke-width="2.5"/><text x="59" y="67" text-anchor="middle" font-size="11" fill="var(--gold)" font-family="Signika,sans-serif">$</text></svg>
      Loans Offered<br>Nationwide
    </div>
    <div class="feature" style="left:349px;top:28px">
      <svg class="badge" viewBox="0 0 118 118"><circle cx="59" cy="59" r="48" fill="none" stroke="#fff" stroke-width="4"/>
        <rect x="37" y="38" width="44" height="40" rx="3" fill="none" stroke="#fff" stroke-width="3"/><rect x="37" y="38" width="44" height="9" fill="#fff"/>
        <g fill="#fff"><rect x="42" y="51" width="7" height="6"/><rect x="52" y="51" width="7" height="6"/><rect x="62" y="51" width="7" height="6"/><rect x="72" y="51" width="5" height="6"/><rect x="42" y="61" width="7" height="6"/><rect x="52" y="61" width="7" height="6"/><rect x="62" y="61" width="7" height="6"/><rect x="42" y="70" width="7" height="5"/><rect x="52" y="70" width="7" height="5"/></g></svg>
      3-5 Day<br>Close
    </div>
    <div class="feature" style="left:501px;top:130px">
      <svg class="badge" viewBox="0 0 118 118"><circle cx="59" cy="59" r="48" fill="none" stroke="#fff" stroke-width="4"/>
        <g fill="#fff"><rect x="38" y="46" width="6" height="30"/><rect x="47" y="54" width="6" height="22"/><rect x="56" y="60" width="6" height="16"/><rect x="65" y="66" width="6" height="10"/><rect x="74" y="70" width="6" height="6"/></g>
        <path d="M46 36 L74 44" stroke="#fff" stroke-width="2.5"/><path d="M70 39 L79 45 L69 48Z" fill="#fff"/></svg>
      Rates as Low<br>as 7%
    </div>
    <div class="feature" style="left:662px;top:28px">
      <svg class="badge" viewBox="0 0 118 118"><circle cx="59" cy="59" r="48" fill="none" stroke="#fff" stroke-width="4"/>
        <path d="M34 58 L54 40 L74 58 L69 58 L69 76 L39 76 L39 58Z" fill="#fff"/>
        <circle cx="72" cy="56" r="8" fill="#fff" stroke="var(--gold)" stroke-width="2"/><path d="M58 78 Q60 64 72 64 Q84 64 86 78Z" fill="#fff" stroke="var(--gold)" stroke-width="2"/></svg>
      Up to 100% of<br>Purchase &amp; Rehab
    </div>
  </div>

  <div class="brand"><span class="dot"></span>Bright Lane Funding</div>

  <div class="contact">
    <p class="lead">Contact us today for more information at:</p>
    <p class="phone">(800) 647-2915 x42</p>
    <p class="email">or email us at: <b>mwelton@brightlanefunding.example</b></p>
    <p class="nmls">NMLS #731856</p>
  </div>

  <svg class="footer-band" viewBox="0 0 993 125" preserveAspectRatio="none">
    <defs><linearGradient id="bandGrad" x1="0" x2="1" y1="0" y2="0">
      <stop offset="0" stop-color="var(--blue-deep)"/><stop offset=".5" stop-color="var(--blue-light)"/><stop offset="1" stop-color="var(--blue-deep)"/></linearGradient></defs>
    <path d="M0 22 Q500 40 993 0 L993 125 L0 125Z" fill="url(#bandGrad)"/>
    <path d="M0 22 Q500 40 993 0" fill="none" stroke="var(--gold)" stroke-width="4"/>
  </svg>
  <p class="website">www.brightlanefunding.example</p>
</div>
</body>
</html>
```